Complete the design for a website wireframe

I need someone to follow the attached wireframe and update the design including icons, pictures and graphics to compliment the copy. I want to have good transitions between sections. All items need to be included as separate files.

Target Market(s)

IT Executives

Number of Pages Required

3 page

Colors
0054AA
0677BA
7BADD7
CADEEF
E8F1F8
F0912C
F2A743
F7CA91
FBE8D2
FDF5EE

```html
<!DOCTYPE html>
<html lang="en">
<head>
<meta charset="utf-8">
<title>Nuvia Solutions</title>
<link rel="stylesheet" href="https://fonts.googleapis.com/css2?family=Barlow:wght@500;600;700&family=Lato:wght@400;700&display=swap">
<style>
:root{
  --blue-dark:#0054AA;
  --blue:#0677BA;
  --blue-mid:#7BADD7;
  --blue-light:#CADEEF;
  --blue-pale:#E8F1F8;
  --sky:#3FA9F0;
  --orange:#F0912C;
  --orange-2:#F2A743;
  --orange-soft:#F7CA91;
  --orange-pale:#FBE8D2;
  --cream:#FDF5EE;
  --ink:#1d1d1f;
  --text:#333;
  --white:#fff;
}
*{box-sizing:border-box;margin:0;padding:0}
html,body{width:1200px;height:4307px;overflow:hidden}
body{font-family:"Lato",sans-serif;color:var(--text);background:var(--white);font-size:12px;line-height:1.5}
h1,h2,h3,h4{font-family:"Barlow",sans-serif}
section,header,footer{position:relative;width:1200px}
.btn{display:inline-block;font-family:"Lato",sans-serif;font-weight:700;font-size:11px;color:#fff;background:var(--orange);border-radius:20px;padding:8px 24px;text-decoration:none}
.btn-blue{background:var(--sky)}
.eyebrow{font-family:"Barlow",sans-serif;color:var(--sky);font-size:18px;font-weight:500;text-align:center}
.title{font-family:"Barlow",sans-serif;color:var(--blue-dark);font-size:36px;font-weight:600;text-align:center;line-height:1.2}
.ph{display:block}

/* header */
.site-header{height:74px;display:flex;align-items:center;justify-content:space-between;padding:0 200px;border-bottom:1px solid #eee}
.brand{display:flex;align-items:center;gap:10px;font-family:"Barlow",sans-serif;font-weight:700;font-size:26px;color:var(--blue-dark)}
.brand-dot{width:44px;height:44px;border-radius:50%;background:var(--sky)}
.nav{display:flex;align-items:center;gap:34px;font-family:"Barlow",sans-serif;font-weight:600;font-size:13px;color:var(--ink)}
.nav .active{color:var(--orange)}

/* hero */
.hero{height:500px;background:linear-gradient(135deg,#1b2d44,#2e4a6b 45%,#1a2a3f);text-align:center;color:#fff}
.hero-mark{padding-top:118px;font-family:"Barlow",sans-serif;font-weight:700;font-size:40px;letter-spacing:1px}
.hero h1{font-size:38px;font-weight:600;margin-top:22px}
.hero p{font-size:17px;margin-top:6px}
.hero .btn{margin-top:24px;padding:9px 24px}
.benefit-bar{position:absolute;left:94px;top:469px;width:1012px;height:62px;background:var(--sky);display:flex;justify-content:space-around;align-items:center;color:#fff;font-family:"Barlow",sans-serif;font-weight:600;font-size:17px}
.benefit-bar span{display:flex;align-items:center;gap:10px}

/* overwhelm */
.overwhelm{height:392px;padding-top:87px;text-align:center}
.overwhelm .lead{font-weight:700;font-size:13px;color:var(--ink);margin-top:16px}
.overwhelm .sub{font-size:13px;margin-top:12px;line-height:1.45}
.feature-row{display:flex;justify-content:center;margin-top:26px}
.feature{width:207px;padding:0 10px;border-right:1px solid #ddd}
.feature:last-child{border-right:0}
.feature-icon{display:block;width:64px;height:56px;margin:0 auto}
.feature h4{font-family:"Lato",sans-serif;font-weight:700;font-size:13px;color:var(--ink);margin-top:12px;line-height:1.35}

/* vetted */
.vetted{height:588px;background:var(--blue-pale);padding-top:60px}
.vetted .title{margin-top:8px}
.split{display:flex;gap:35px;margin:23px 0 0 200px;width:800px}
.vetted-photo{width:338px;height:374px;flex:none;background:linear-gradient(135deg,#3b3a46,#a08a6a 50%,#d9c7a4);box-shadow:0 2px 8px rgba(0,0,0,.15)}
.copy{font-size:12px;color:var(--text);padding-top:26px;width:400px}
.copy p{margin-bottom:13px}
.copy strong{color:var(--ink)}
.checks{list-style:none;margin-bottom:18px}
.checks li{display:flex;align-items:center;gap:8px;font-weight:700;color:var(--ink);margin-bottom:6px}

/* support */
.support{height:548px;padding-top:62px}
.cards{display:flex;justify-content:space-between;width:800px;margin:28px auto 0}
.card{width:250px;text-align:center}
.card-img{height:188px}
.card h4{font-family:"Lato",sans-serif;font-size:13px;font-weight:700;color:var(--ink);margin-top:20px}
.card p{font-size:10px;margin-top:12px;line-height:1.5;padding:0 10px}
.card a{display:block;font-size:10.5px;font-weight:700;color:var(--blue);margin-top:14px;text-decoration:none}
.card a.orange{color:var(--orange)}

/* partners */
.partners{height:224px;background:var(--blue-dark);padding-top:40px}
.partners .title{color:#fff}
.badges{display:flex;justify-content:space-between;width:800px;margin:26px auto 0}
.badge{width:150px;height:68px;background:#fff;border-radius:3px;display:flex;align-items:center;justify-content:center;gap:10px}
.badge-shape{width:26px;height:26px;border-radius:50%;background:var(--blue-light)}
.badge-bar{width:70px;height:12px;border-radius:6px;background:var(--blue-pale)}
.badge.alt .badge-shape{background:var(--orange-soft);border-radius:4px}

/* how */
.how{height:475px;background:var(--blue-pale);padding-top:60px;text-align:center}
.steps{display:flex;justify-content:space-between;width:660px;margin:26px auto 0}
.step{width:220px}
.step-icon{display:block;width:84px;height:84px;margin:0 auto}
.step h4{font-family:"Lato",sans-serif;font-size:16px;font-weight:700;color:var(--ink);margin-top:12px}
.step p{font-size:10.5px;margin-top:10px;line-height:1.5}
.how .btn{margin-top:26px}
.how .link{display:block;color:var(--blue);font-size:13px;margin-top:10px}

/* advisor */
.advisor{height:555px;padding-top:58px}
.advisor-body{display:flex;justify-content:space-between;width:800px;margin:30px auto 0}
.advisor .copy{width:385px;padding-top:30px}
.advisor .copy p{margin-bottom:16px}
.advisor-photo{width:388px;height:374px;background:linear-gradient(135deg,#cfd7df,#eef1f4 50%,#9aa6b4);box-shadow:0 2px 8px rgba(0,0,0,.15)}

/* growth band */
.growth{height:187px;background:linear-gradient(90deg,#1f7cc9,#3aa2e6 50%,#1f7cc9);color:#fff;text-align:center;padding-top:40px}
.growth h2{font-size:36px;font-weight:600}
.growth p{font-size:13px;font-weight:700;margin-top:6px;line-height:1.75}

/* spotlight */
.spotlight{height:394px;padding-top:62px}
.spot-body{display:flex;gap:25px;width:800px;margin-left:200px}
.spot-art{position:relative;width:388px;height:270px;flex:none}
.spot-a{position:absolute;left:0;top:0;width:206px;height:206px;background:linear-gradient(135deg,#0d3c66,#2a8fc7)}
.spot-b{position:absolute;left:181px;top:62px;width:207px;height:207px;background:linear-gradient(135deg,#f2a743,#b8521c 60%,#3a2a3a);border:3px solid #fff}
.spot-copy{width:387px;padding-top:8px}
.spot-copy h3{font-size:28px;font-weight:600;color:var(--blue-dark)}
.spot-copy p{font-size:11.5px;margin-top:10px;line-height:1.6}
.spot-copy .btn{margin-top:20px}

/* footer */
.site-footer{height:321px;background:var(--blue-pale);text-align:center;padding-top:48px}
.site-footer .brand{justify-content:center;font-size:30px}
.site-footer .about{font-size:13px;margin:30px auto 0;width:520px;line-height:1.5}
.footer-nav{display:flex;align-items:center;justify-content:center;gap:36px;margin-top:22px;font-weight:700;font-size:11px;color:var(--ink)}
.footer-nav .rule{width:128px;height:1px;background:#bbb}
.site-footer .btn{margin-top:26px}
.bottom-bar{height:49px;background:#0d0f12;color:#fff;display:flex;align-items:center;justify-content:space-between;padding:0 200px;font-size:11px}
.bottom-bar em{font-style:normal;color:var(--sky)}
.social{display:flex;gap:10px}
.social span{width:30px;height:30px;border-radius:50%}
</style>
</head>
<body>

<header class="site-header">
  <div class="brand"><span class="brand-dot"></span>Nuvia</div>
  <nav class="nav">
    <span class="active">Home</span><span>Services ⌄</span><span>About</span><span>People</span>
    <a class="btn btn-blue" href="#">Schedule a Call</a>
  </nav>
</header>

<section class="hero" role="img" aria-label="Dark blue photo of hands working with a digital technology interface">
  <div class="hero-mark">Nuvia</div>
  <h1>Get Clarity on Your Technology Roadmap</h1>
  <p>Partner with a Trusted Advisor for Voice, Data, Cloud and Security Solutions</p>
  <a class="btn" href="#">Schedule a Call</a>
  <div class="benefit-bar">
    <span><svg width="16" height="16" viewBox="0 0 16 16"><circle cx="8" cy="8" r="7" fill="none" stroke="#fff" stroke-width="1.4"/><path d="M4.5 8.2l2.3 2.2 4.7-4.6" fill="none" stroke="#fff" stroke-width="1.4"/></svg>Stay Ahead of Disruption</span>
    <span><svg width="16" height="16" viewBox="0 0 16 16"><circle cx="8" cy="8" r="7" fill="none" stroke="#fff" stroke-width="1.4"/><path d="M4.5 8.2l2.3 2.2 4.7-4.6" fill="none" stroke="#fff" stroke-width="1.4"/></svg>Outpace the Competition</span>
    <span><svg width="16" height="16" viewBox="0 0 16 16"><circle cx="8" cy="8" r="7" fill="none" stroke="#fff" stroke-width="1.4"/><path d="M4.5 8.2l2.3 2.2 4.7-4.6" fill="none" stroke="#fff" stroke-width="1.4"/></svg>Lead Future Growth</span>
  </div>
</section>

<section class="overwhelm">
  <h2 class="title">Technology Shouldn't Be Overwhelming</h2>
  <p class="lead">Many business leaders struggle to keep pace with rapidly changing technology.</p>
  <p class="sub">Thousands of tech companies offer innovative solutions. But finding the RIGHT provider is overwhelming<br>when you aren't certain you will:</p>
  <div class="feature-row">
    <div class="feature">
      <svg class="feature-icon" viewBox="0 0 64 56" role="img" aria-label="Price tag icon">
        <path d="M20 20h22l14 14-16 16-20-20z" fill="var(--orange)"/>
        <circle cx="27" cy="26" r="3" fill="#fff"/>
        <text x="40" y="40" font-family="Lato,sans-serif" font-weight="700" font-size="14" fill="#fff" text-anchor="middle">$</text>
        <rect x="6" y="30" width="9" height="20" rx="2" fill="var(--orange-2)"/>
      </svg>
      <h4>Receive the best price<br>and value</h4>
    </div>
    <div class="feature">
      <svg class="feature-icon" viewBox="0 0 64 56" role="img" aria-label="Connected blocks icon">
        <path d="M32 14v14M18 28h28M18 28v10M46 28v10" stroke="var(--orange-2)" stroke-width="3" fill="none"/>
        <rect x="24" y="2" width="16" height="14" rx="2" fill="var(--orange)"/>
        <rect x="10" y="36" width="16" height="14" rx="2" fill="var(--orange)"/>
        <rect x="38" y="36" width="16" height="14" rx="2" fill="var(--orange)"/>
        <rect x="27" y="24" width="10" height="9" rx="2" fill="var(--orange-2)"/>
      </svg>
      <h4>Successfully integrate<br>the new solution</h4>
    </div>
    <div class="feature">
      <svg class="feature-icon" viewBox="0 0 64 56" role="img" aria-label="Support headset icon">
        <path d="M14 30a18 18 0 0 1 36 0" stroke="var(--orange)" stroke-width="4" fill="none"/>
        <rect x="10" y="28" width="10" height="16" rx="4" fill="var(--orange)"/>
        <rect x="44" y="28" width="10" height="16" rx="4" fill="var(--orange)"/>
        <rect x="22" y="20" width="20" height="16" rx="4" fill="var(--orange-2)"/>
        <circle cx="27" cy="28" r="1.8" fill="#fff"/><circle cx="32" cy="28" r="1.8" fill="#fff"/><circle cx="37" cy="28" r="1.8" fill="#fff"/>
        <path d="M49 44c0 6-6 8-13 8" stroke="var(--orange)" stroke-width="3" fill="none"/>
      </svg>
      <h4>Receive expert ongoing<br>support</h4>
    </div>
    <div class="feature">
      <svg class="feature-icon" viewBox="0 0 64 56" role="img" aria-label="Growth arrow icon">
        <rect x="12" y="36" width="9" height="14" rx="1" fill="var(--orange-2)"/>
        <rect x="27" y="28" width="9" height="22" rx="1" fill="var(--orange)"/>
        <rect x="42" y="20" width="9" height="30" rx="1" fill="var(--orange-2)"/>
        <path d="M10 28l16-12 8 6 16-14" stroke="var(--orange)" stroke-width="3" fill="none"/>
        <path d="M44 6h8v8" stroke="var(--orange)" stroke-width="3" fill="none"/>
      </svg>
      <h4>Invest in a solution that<br>remains relevant</h4>
    </div>
  </div>
</section>

<section class="vetted">
  <p class="eyebrow">Streamline Your Business With</p>
  <h2 class="title">Expert-Vetted Tech Solutions</h2>
  <div class="split">
    <div class="vetted-photo ph" role="img" aria-label="Photo of a hand holding a glowing light bulb surrounded by gears"></div>
    <div class="copy">
      <p>At Nuvia, we understand how frustrating working with technology providers can be.</p>
      <p>Not only do you face time-consuming meetings and demos...</p>
      <p>You also risk investing in a solution that won't deliver as promised.</p>
      <p><strong>Our process takes the headache out of sourcing the RIGHT tech solutions for your business.</strong></p>
      <p>You get a custom plan to implement at every stage, so you can:</p>
      <ul class="checks">
        <li><svg width="13" height="13" viewBox="0 0 16 16"><circle cx="8" cy="8" r="7" fill="none" stroke="#3FA9F0" stroke-width="1.5"/><path d="M4.5 8.2l2.3 2.2 4.7-4.6" fill="none" stroke="#3FA9F0" stroke-width="1.5"/></svg>Protect against security threats</li>
        <li><svg width="13" height="13" viewBox="0 0 16 16"><circle cx="8" cy="8" r="7" fill="none" stroke="#3FA9F0" stroke-width="1.5"/><path d="M4.5 8.2l2.3 2.2 4.7-4.6" fill="none" stroke="#3FA9F0" stroke-width="1.5"/></svg>Stay ahead of your competition</li>
        <li><svg width="13" height="13" viewBox="0 0 16 16"><circle cx="8" cy="8" r="7" fill="none" stroke="#3FA9F0" stroke-width="1.5"/><path d="M4.5 8.2l2.3 2.2 4.7-4.6" fill="none" stroke="#3FA9F0" stroke-width="1.5"/></svg>Stay ahead of your competition</li>
      </ul>
      <a class="btn" href="#">More on the Process</a>
    </div>
  </div>
</section>

<section class="support">
  <p class="eyebrow">Custom Solutions and</p>
  <h2 class="title">Support At Every Stage</h2>
  <div class="cards">
    <div class="card">
      <div class="card-img ph" role="img" aria-label="Photo of hands at a keyboard with glowing digital icons" style="background:linear-gradient(135deg,#3a2a22,#c8742e 55%,#1f2c3f)"></div>
      <h4>Digital Transformation</h4>
      <p>Need to upgrade a legacy solution or invest in a new one? We'll help you create a custom plan for a seamless transition.</p>
      <a href="#">Get a Roadmap for Transformation</a>
    </div>
    <div class="card">
      <div class="card-img ph" role="img" aria-label="Photo of a hand holding a glowing security shield" style="background:linear-gradient(135deg,#0b1e33,#2d5d86 55%,#0b1e33)"></div>
      <h4>Secure Your Business</h4>
      <p>Leverage our expertise to identify the systems and tools needed to scale your business with confidence.</p>
      <a class="orange" href="#">Learn How To Protect Your Business</a>
    </div>
    <div class="card">
      <div class="card-img ph" role="img" aria-label="Photo of a finger touching a glowing blue technology interface" style="background:linear-gradient(135deg,#061a2e,#1f6f9a 55%,#08213a)"></div>
      <h4>Optimize Expenses</h4>
      <p>Ready to optimize, but unsure where to start? We'll help you pinpoint existing tech obstacles, create a custom plan and set you up with the best deal at a great price.</p>
      <a href="#">Get A Detailed Analysis</a>
    </div>
  </div>
</section>

<section class="partners">
  <h2 class="title">Our Trusted Partners...</h2>
  <div class="badges">
    <div class="badge" role="img" aria-label="Partner badge"><span class="badge-shape"></span><span class="badge-bar"></span></div>
    <div class="badge alt" role="img" aria-label="Partner badge"><span class="badge-shape"></span><span class="badge-bar"></span></div>
    <div class="badge" role="img" aria-label="Partner badge"><span class="badge-shape"></span><span class="badge-bar"></span></div>
    <div class="badge alt" role="img" aria-label="Partner badge"><span class="badge-shape"></span><span class="badge-bar"></span></div>
    <div class="badge" role="img" aria-label="Partner badge"><span class="badge-shape"></span><span class="badge-bar"></span></div>
  </div>
</section>

<section class="how">
  <p class="eyebrow">Here's How To</p>
  <h2 class="title">Make Tech Decisions with Confdence</h2>
  <div class="steps">
    <div class="step">
      <svg class="step-icon" viewBox="0 0 84 84" role="img" aria-label="Phone and calendar icon">
        <rect x="8" y="14" width="30" height="58" rx="5" fill="none" stroke="var(--ink)" stroke-width="3"/>
        <line x1="18" y1="64" x2="28" y2="64" stroke="var(--ink)" stroke-width="3"/>
        <circle cx="23" cy="38" r="10" fill="none" stroke="var(--orange)" stroke-width="3"/>
        <path d="M23 32v6h5" stroke="var(--orange)" stroke-width="3" fill="none"/>
        <rect x="44" y="28" width="32" height="28" rx="3" fill="var(--orange-2)" stroke="var(--ink)" stroke-width="3"/>
        <line x1="44" y1="36" x2="76" y2="36" stroke="var(--ink)" stroke-width="3"/>
        <path d="M53 46l4 4 9-9" stroke="#fff" stroke-width="3" fill="none"/>
      </svg>
      <h4>Schedule a Call</h4><p>We'll take time to understand your unique needs, then determine your best next steps.</p>
    </div>
    <div class="step">
      <svg class="step-icon" viewBox="0 0 84 84" role="img" aria-label="Cloud and server icon">
        <path d="M24 38a12 12 0 0 1 4-23 16 16 0 0 1 30 4 10 10 0 0 1 2 19z" fill="none" stroke="var(--ink)" stroke-width="3"/>
        <line x1="42" y1="38" x2="42" y2="48" stroke="var(--ink)" stroke-width="3"/>
        <rect x="24" y="48" width="36" height="10" rx="2" fill="var(--orange-2)" stroke="var(--ink)" stroke-width="3"/>
        <rect x="24" y="60" width="36" height="10" rx="2" fill="var(--orange)" stroke="var(--ink)" stroke-width="3"/>
        <circle cx="31" cy="53" r="1.8" fill="var(--ink)"/><circle cx="31" cy="65" r="1.8" fill="var(--ink)"/>
      </svg>
      <h4>Develop a Roadmap</h4><p>With our outcome-driven approach, you get a clear plan and implementation at every stage.</p>
    </div>
    <div class="step">
      <svg class="step-icon" viewBox="0 0 84 84" role="img" aria-label="Upward growth arrow icon">
        <circle cx="42" cy="42" r="32" fill="none" stroke="var(--ink)" stroke-width="3"/>
        <path d="M24 58l14-14 8 8 16-18" stroke="var(--orange)" stroke-width="4" fill="none"/>
        <path d="M52 34h10v10" stroke="var(--orange)" stroke-width="4" fill="none"/>
      </svg>
      <h4>Lead Future Growth</h4><p>Confidently grow your business and stay ahead of disruption and the competition.</p>
    </div>
  </div>
  <a class="btn btn-blue" href="#">Schedule a Call</a>
  <span class="link">Take Back Your Time</span>
</section>

<section class="advisor">
  <h2 class="title">How Will an IT Advisor Help You?</h2>
  <div class="advisor-body">
    <div class="copy">
      <p>Do you really want to vet and negotiate with each service provider yourself?</p>
      <p>A trusted IT advisor reduces the time and energy it takes to source and implement tech solutions.</p>
      <p>We'll take the time to know your business and understand your needs.</p>
      <p>Then, we'll use our objective, in-depth approach to fnd the BEST solution for your business, at a great price.</p>
      <p>You'll walk away with a custom roadmap to easily implement your new tech solution.</p>
      <p>Plus, leverage our expert support at any time if you run into snags with your provider.</p>
      <a class="btn" href="#">Meet Dana</a>
    </div>
    <div class="advisor-photo ph" role="img" aria-label="Photo of hands reviewing charts and a tablet on a desk"></div>
  </div>
</section>

<section class="growth" role="img" aria-label="Bright blue abstract technology background">
  <h2>Secure Future Business Growth</h2>
  <p>Don't wait another day. There's too much at risk. Get the direction you need to streamline internal processes.<br>Create an exceptional experience for customers AND employees.</p>
</section>

<section class="spotlight">
  <div class="spot-body">
    <div class="spot-art">
      <div class="spot-a" role="img" aria-label="Photo of a person using a phone with chat icons"></div>
      <div class="spot-b" role="img" aria-label="Orange graphic about lead generation"></div>
    </div>
    <div class="spot-copy">
      <h3>Spotlight Lead Generator</h3>
      <p>Lorem Ipsum is simply dummy text of the printing and typesetting industry. Lorem Ipsum has been the industry's standard dummy text ever since the 1500s.</p>
      <p>When an unknown printer took a galley of type and scrambled it to make a type specimen book. It has survived not only five centuries, but also the leap into electronic typesetting, containing lorem Ipsum.</p>
      <a class="btn btn-blue" href="#">Download Now</a>
    </div>
  </div>
</section>

<footer class="site-footer">
  <div class="brand"><span class="brand-dot"></span>Nuvia</div>
  <p class="about">Helping business leaders source and implement custom technology solutions to stay ahead of disruption and outpace their competition.</p>
  <div class="footer-nav">
    <span class="rule"></span><span>Services</span><span>Solutions</span><span>Process</span><span>About</span><span>Contact</span><span>Case Study</span><span>Partners</span><span class="rule"></span>
  </div>
  <a class="btn btn-blue" href="#">Schedule a Call</a>
</footer>
<div class="bottom-bar">
  <span>© 2022 <em>Nuvia Solutions</em>. All Right Reserved</span>
  <div class="social"><span style="background:var(--sky)"></span><span style="background:var(--orange)"></span><span style="background:var(--sky)"></span></div>
</div>

</body>
</html>
```